Professional individual needs business card design

I need a business card designed for my friend to show their skills and contact details

I would like to see pattern designs with a black foreground and strong look - will submit content specifics but basics are:

NAME SURNAME (large and bold)
Event Manager & MC

Tressel Magazine
The other event I run

phone number - email

```html
<!DOCTYPE html>
<html lang="en">
<head>
<meta charset="utf-8">
<title>Business Card – Event Manager &amp; MC</title>
<link rel="stylesheet" href="https://fonts.googleapis.com/css2?family=Ubuntu:ital,wght@0,400;1,300&family=Ubuntu+Condensed&display=swap">
<style>
  :root {
    --page-bg: #ffffff;
    --card-bg: #000000;
    --ink: #ffffff;
    --rule: #6a6a6a;
  }
  html, body {
    margin: 0;
    padding: 0;
    width: 1200px;
    height: 988px;
    overflow: hidden;
    background: var(--page-bg);
  }
  .canvas {
    position: relative;
    width: 1200px;
    height: 988px;
  }
  .card {
    position: absolute;
    left: 321px;
    top: 277px;
    width: 528px;
    height: 315px;
    background: var(--card-bg);
    color: var(--ink);
    font-family: "Ubuntu", sans-serif;
  }
  .brand {
    position: absolute;
    left: 37px;
    top: 28px;
    width: 114px;
    height: 114px;
  }
  .brand-ring {
    position: absolute;
    inset: 0;
  }
  .brand-name {
    position: absolute;
    inset: 0;
    display: flex;
    align-items: center;
    justify-content: center;
    font-family: "Ubuntu", sans-serif;
    font-weight: 400;
    font-size: 21px;
    letter-spacing: 0.5px;
    color: var(--ink);
  }
  .identity {
    position: absolute;
    left: 37px;
    top: 192px;
    margin: 0;
    font-family: "Ubuntu Condensed", sans-serif;
    font-weight: 400;
    font-size: 21px;
    line-height: 27px;
  }
  .identity .person-name,
  .identity .person-role {
    display: block;
  }
  .venture {
    position: absolute;
    left: 346px;
    top: 100px;
    margin: 0;
    font-family: "Ubuntu", sans-serif;
    font-style: italic;
    font-weight: 300;
    font-size: 13px;
    line-height: 17px;
  }
  .venture span { display: block; }
  .divider {
    position: absolute;
    left: 5px;
    top: 263px;
    width: 514px;
    height: 1px;
    background: var(--rule);
  }
  .contact {
    position: absolute;
    top: 282px;
    display: flex;
    align-items: center;
    gap: 10px;
    font-family: "Ubuntu Condensed", sans-serif;
    font-size: 13px;
    line-height: 18px;
  }
  .contact svg { width: 17px; height: 17px; flex: none; }
  .contact-phone { left: 80px; }
  .contact-email { left: 302px; }
</style>
</head>
<body>
<div class="canvas">
  <section class="card">
    <div class="brand">
      <svg class="brand-ring" viewBox="0 0 114 114" aria-hidden="true">
        <circle cx="57" cy="57" r="54" fill="none" stroke="#ffffff" stroke-width="3"/>
      </svg>
      <span class="brand-name">LOGO</span>
    </div>

    <p class="venture">
      <span>Tressel Magazine</span>
      <span>The other event I run</span>
    </p>

    <h1 class="identity">
      <span class="person-name">NAME SURNAME</span>
      <span class="person-role">Event Manager &amp; MC</span>
    </h1>

    <div class="divider"></div>

    <div class="contact contact-phone">
      <svg viewBox="0 0 20 20" aria-hidden="true">
        <circle cx="10" cy="10" r="9" fill="none" stroke="#ffffff" stroke-width="1.2"/>
        <path d="M6.5 5.5 l2 0 l0.8 2.3 l-1.2 1 q1 2 3 3 l1 -1.2 l2.3 0.8 l0 2 q-0.5 1 -1.8 0.9 q-3.5 -0.6 -5.9 -4.3 q-1.2 -2.2 -0.2 -4.5 z" fill="none" stroke="#ffffff" stroke-width="1.1" stroke-linejoin="round"/>
      </svg>
      <span>0000-0000-0000</span>
    </div>

    <div class="contact contact-email">
      <svg viewBox="0 0 20 20" aria-hidden="true">
        <circle cx="10" cy="10" r="9" fill="none" stroke="#ffffff" stroke-width="1.2"/>
        <rect x="5.5" y="7" width="9" height="6" fill="#ffffff"/>
        <path d="M5.5 7 l4.5 3.5 l4.5 -3.5" fill="none" stroke="#000000" stroke-width="1"/>
      </svg>
      <span>yourmail@mail.com</span>
    </div>
  </section>
</div>
</body>
</html>
```